Surgical Procedure Room Letterhead

PLEASE DO NOT MAKE YOUR LETTERHEAD SIMILAR TO THE ONE I AM INCLUDING IN MY UPLOADS

Hello! I need my logo used to make a very clean, professional, simple letterhead that has all the pertinent information in it:
Location: 4829 NW 58th Lane, Suite 310
Marlow Bay, GA 33468
Phone: 954-618-2450
Fax: 800-394-8261

Can you please put this all on a word document that is easily editable? I will include my practice letterhead as an example ONLY of how easy it should be to write below the letterhead. Please don't make this letterhead the same as the one I am including in this example. They are two separate businesses.

Target Market(s)

Insurance companies

Industry/Entity Type

medical

Requirements
Must have
• classiness, elegance, simplicity
Should not have
• Please don't make your letterhead the same as the one that I included in my uploads

```html
<!DOCTYPE html>
<html lang="en">
<head>
<meta charset="utf-8">
<title>Verity Procedure Suites – Letterhead</title>
<link href="https://fonts.googleapis.com/css2?family=Open+Sans:wght@400;600&display=swap" rel="stylesheet">
<style>
  :root {
    --backdrop: #8b8b8b;
    --paper: #ffffff;
    --gold: #d9b33d;
    --navy: #1b3560;
  }
  html, body {
    margin: 0;
    width: 1200px;
    height: 686px;
    overflow: hidden;
    background: var(--backdrop);
    font-family: "Open Sans", Arial, sans-serif;
  }
  .letterhead {
    position: absolute;
    left: 370px;
    top: 18px;
    width: 460px;
    height: 650px;
    background: var(--paper);
    overflow: hidden;
    box-shadow: 0 4px 14px rgba(0,0,0,0.25);
  }
  .brand {
    position: absolute;
    left: 34px;
    top: 36px;
    display: flex;
    align-items: center;
    gap: 8px;
  }
  .brand-dot {
    width: 18px;
    height: 18px;
    border-radius: 50%;
    background: var(--gold);
  }
  .brand-name {
    font-weight: 600;
    font-size: 15px;
    letter-spacing: 1.2px;
    text-transform: uppercase;
    color: var(--navy);
    line-height: 1.15;
  }
  .contact {
    position: absolute;
    right: 28px;
    top: 96px;
    padding-left: 12px;
    border-left: 1.5px solid var(--gold);
    font-style: normal;
    font-size: 9px;
    line-height: 1.5;
  }
  .contact-row {
    display: flex;
    align-items: flex-start;
    gap: 5px;
  }
  .contact-row svg { width: 8px; height: 8px; margin-top: 2.5px; fill: var(--gold); flex: none; }
  .contact-phone { color: var(--navy); }
  .contact-address { color: var(--gold); }
  .footer-swoosh {
    position: absolute;
    left: 0;
    top: 0;
    width: 460px;
    height: 650px;
  }
</style>
</head>
<body>
  <main class="letterhead">
    <div class="brand">
      <span class="brand-dot"></span>
      <span class="brand-name">Verity Procedure<br>Suites</span>
    </div>

    <address class="contact">
      <div class="contact-row contact-phone">
        <svg viewBox="0 0 10 10" aria-hidden="true"><path d="M2 0.5 L3.6 2.6 L2.8 3.6 Q4 6 6.4 7.2 L7.4 6.4 L9.5 8 L8.4 9.5 Q3 9 0.5 1.6 Z"/></svg>
        <span>555-618-2450</span>
      </div>
      <div class="contact-row contact-phone">
        <svg viewBox="0 0 10 10" aria-hidden="true"><rect x="2.5" y="0.5" width="5" height="3"/><rect x="0.5" y="3.5" width="9" height="5" rx="1"/><rect x="2.5" y="6" width="5" height="3.5" fill="#fff"/></svg>
        <span>833-394-8261</span>
      </div>
      <div class="contact-row contact-address">
        <svg viewBox="0 0 10 10" aria-hidden="true"><path d="M5 0.3 A3.4 3.4 0 0 1 8.4 3.7 C8.4 6 5 9.7 5 9.7 C5 9.7 1.6 6 1.6 3.7 A3.4 3.4 0 0 1 5 0.3 Z M5 2.4 A1.3 1.3 0 1 0 5 5 A1.3 1.3 0 1 0 5 2.4 Z"/></svg>
        <span>4829 NW 58th Lane,<br>Suite 310, Marlow Bay, GA 33468</span>
      </div>
    </address>

    <svg class="footer-swoosh" viewBox="0 0 460 650" aria-hidden="true">
      <path d="M0 594 C 110 620 290 642 446 650 L0 650 Z" fill="var(--gold)"/>
      <path d="M170 622 C 280 636 380 645 460 648" fill="none" stroke="var(--navy)" stroke-width="3"/>
    </svg>
  </main>
</body>
</html>
```